Serial Entrepreneur Business Card: 4 Logo Design

I am a serial entrepreneur and a full time mechanical engineer. I have four businesses. I would like to display them all on one business card.
*Please see the attached PDF for the design requirements*

www.KelbroNest.com

Businesses
-KelbroNest
-Quiet Lantern Properties
-Torlen Products
-Drosk Harbor Cast

Target Market(s)

Clients, Entrepreneurs, Associates, really anyone. Should be very professional.

Industry/Entity Type

Entrepreneur

Contact Information for Business Card

3.5" x 2" Standard Business Card Size
** Please review the attached requirement PDF for in depth detail on what I am expecting**

Font styles to use
Sans Serif

Requirements
Must have
• My personal contact information:
• First Name: Dae hwan
• Last Name: Pellow
• Nick Name: Riko
• Address: 83 Tolmer Court, Garfield NJ 07392
• Phone Number: 201-574-2916
• Email: RikodPellow@mailnest.example
• Website: www.KelbroNest.com
• All Four Logos of the Companies I own:
• -KelbroNest
• -Quiet Lantern Properties
• -Torlen Products
• -Drosk Harbor Cast
• My Professions:
• -Prototyping Engineer
• -Real Estate Investor
• -Financial Blogger
• -Video Podcaster
• -Online Retail Seller
Nice to have
• If it fits, please include the website for each logo, if there is more space please include the email for each.
• It might be nice to have the QX GUILD Logo, or TOVRA logo for my full-time job. But only if it fits.

```html
<!DOCTYPE html>
<html lang="en">
<head>
<meta charset="utf-8">
<title>Dae hwan "Riko" Pellow – Business Card</title>
<link rel="stylesheet" href="https://fonts.googleapis.com/css2?family=Roboto:wght@400;700&family=Roboto+Condensed:wght@400;700&display=swap">
<style>
  :root {
    --bg: #ececec;
    --card-white: #ffffff;
    --ink: #111111;
    --ink-soft: #222222;
    --brand-green: #1f8a43;
    --band-grey: #eef0f2;
    --tile-dark: #a9a9a9;
    --tile-light: #e7e7e9;
    --rule: #555555;
  }
  * { box-sizing: border-box; margin: 0; padding: 0; }
  html, body { width: 1200px; height: 1000px; overflow: hidden; }
  body {
    background: var(--bg);
    font-family: "Roboto", Arial, sans-serif;
    color: var(--ink);
    position: relative;
  }
  .card {
    position: absolute;
    width: 530px;
    height: 303px;
    box-shadow: 0 4px 14px rgba(0,0,0,0.25);
    overflow: hidden;
  }

  /* Front */
  .card-front { left: 165px; top: 250px; background: var(--card-white); }
  .front-band {
    position: absolute; left: 0; right: 0; bottom: 30px; height: 80px;
    background: var(--band-grey);
    clip-path: polygon(0 55%, 100% 0, 100% 100%, 0 100%);
  }
  .front-corner-square {
    position: absolute; left: 0; bottom: 0; width: 42px; height: 42px;
    background: var(--brand-green);
  }
  .job-badge {
    position: absolute; top: 22px; right: 60px; width: 44px; height: 44px;
    background: var(--ink); border: 3px solid #fff; outline: 2px solid var(--ink);
  }
  .job-bar {
    position: absolute; top: 22px; right: 0; width: 48px; height: 44px;
    background: var(--ink);
  }
  .holder-name {
    position: absolute; left: 40px; top: 96px;
    font-weight: 700; font-size: 19px; color: var(--brand-green);
  }
  .holder-name .nick { color: var(--ink); }
  .professions {
    position: absolute; left: 52px; top: 150px;
    list-style: none; font-size: 14.5px; line-height: 20px;
  }
  .divider {
    position: absolute; left: 228px; top: 146px; width: 1px; height: 108px;
    background: var(--rule);
  }
  .contacts {
    position: absolute; left: 258px; top: 100px;
    list-style: none; font-size: 14.5px; line-height: 20px;
  }

  /* Back */
  .card-back { left: 482px; top: 512px; width: 526px; background: var(--ink); }
  .logo-grid {
    position: absolute; left: 0; right: 0; top: 18px; bottom: 18px;
    display: grid; grid-template-columns: 1fr 1fr; grid-template-rows: 1fr 1fr;
  }
  .venture {
    display: flex; flex-direction: column; align-items: center; justify-content: center;
    font-family: "Roboto Condensed", Arial, sans-serif;
    font-size: 14px; line-height: 17px; letter-spacing: 0.6px; color: var(--ink-soft);
  }
  .venture.dark { background: var(--tile-dark); }
  .venture.light { background: var(--tile-light); }
  .venture-name {
    display: flex; align-items: center; gap: 8px;
    font-family: "Roboto", Arial, sans-serif; font-weight: 700;
    font-size: 19px; letter-spacing: 0; color: var(--ink);
    margin-bottom: 14px;
  }
  .venture-mark { width: 16px; height: 16px; background: var(--ink); }
</style>
</head>
<body>

<section class="card card-front" aria-label="Business card front">
  <div class="front-band"></div>
  <div class="front-corner-square"></div>
  <div class="job-badge" aria-label="Employer badge"></div>
  <div class="job-bar"></div>

  <h1 class="holder-name">Dae hwan <span class="nick">“Riko”</span> Pellow</h1>

  <ul class="professions">
    <li>Prototyping Engineer</li>
    <li>Real Estate Investor</li>
    <li>Financial Blogger</li>
    <li>Video Podcaster</li>
    <li>Online Retail Seller</li>
  </ul>
  <div class="divider"></div>
  <ul class="contacts">
    <li>201-574-2916</li>
    <li>RikodPellow@mailnest.example</li>
    <li>Riko@KelbroNest.com</li>
    <li>www.KelbroNest.com</li>
    <li>83 Tolmer Court, Garfield NJ 07392</li>
  </ul>
</section>

<section class="card card-back" aria-label="Business card back">
  <div class="logo-grid">
    <div class="venture dark">
      <div class="venture-name"><span class="venture-mark"></span>KelbroNest</div>
      <span>www.KelbroNest.com</span>
      <span>Riko@KelbroNest.com</span>
    </div>
    <div class="venture light">
      <div class="venture-name"><span class="venture-mark"></span>Drosk Harbor Cast</div>
      <span>www.DroskHarborCast.com</span>
      <span>Media@DroskHarborCast.com</span>
    </div>
    <div class="venture light">
      <div class="venture-name"><span class="venture-mark"></span>Torlen Products</div>
      <span>www.TorlenProducts.com</span>
      <span>Sales@TorlenProducts.com</span>
    </div>
    <div class="venture dark">
      <div class="venture-name"><span class="venture-mark"></span>Quiet Lantern Properties</div>
      <span>www.QuietLanternProperties.com</span>
      <span>Riko@QuietLanternProperties.com</span>
    </div>
  </div>
</section>

</body>
</html>
```